Tradeshow Banner Design (Qty2, 6'H x 2'W)

Brightwell Contractors is an Electrical, Fire Alarm, and Security Contracting company. For tradeshows, we would like 2 vertical Banners to put behind our booth. Our colors are Red, Grey & Black. I would like the Banners to be informative on what services we provide, with some appealing Graphic Design. (bwc-kmo.com)
Slogan: Safeguarding Communities Electrical, Fire & Security Solutions
Target Market(s)
Commercial Construction Clients
Industry/Entity Type
Electrical / Construction
Font styles to use
Other font styles liked:
- Aileron
Colors
EB3D1F
EC4F4E
F09395
F8D3D4
FCEDEE
Requirements
Must have
- Our Logo, Color Scheme, Brief Caption of the services we provide
Nice to have
- Appealing Imagery & a modern/simplistic design

```html
<!DOCTYPE html>
<html lang="en">
<head>
<meta charset="utf-8">
<title>Brightwell Contractors – Tradeshow Banners</title>
<link rel="stylesheet" href="https://fonts.googleapis.com/css2?family=Montserrat:wght@300;500;600;700;800&display=swap">
<style>
  :root {
    --red: #ec1c24;
    --red-deep: #d31f26;
    --grey-dark: #444446;
    --grey-mid: #58585a;
    --backdrop: #e4e5e7;
    --white: #ffffff;
  }
  * { box-sizing: border-box; margin: 0; padding: 0; }
  html, body {
    width: 1160px; height: 1200px; overflow: hidden;
    background: var(--backdrop);
    font-family: "Montserrat", Arial, sans-serif;
  }
  .stage { position: relative; width: 1160px; height: 1200px; }
  .banner {
    position: absolute; top: 48px;
    width: 367px; height: 1103px;
    background: var(--white); overflow: hidden;
    box-shadow: 0 6px 18px rgba(0,0,0,.18);
  }
  .banner--brand { left: 166px; }
  .banner--services { left: 615px; }
  .banner-shapes { position: absolute; inset: 0; width: 100%; height: 100%; }

  /* Brand banner */
  .brand-mark {
    position: absolute; top: 88px; left: 0; width: 100%;
    display: flex; flex-direction: column; align-items: center; gap: 26px;
  }
  .brand-mark__dot {
    width: 172px; height: 172px; border-radius: 50%; background: var(--red);
  }
  .brand-mark__name {
    color: var(--grey-dark); font-weight: 600; font-size: 25px;
    letter-spacing: .5px; text-align: center; line-height: 1.15;
  }
  .slogan {
    position: absolute; top: 612px; left: 0; width: 100%;
    color: var(--white); font-weight: 600; font-size: 35px;
    line-height: 43px; text-align: center;
  }
  .rule {
    position: absolute; height: 3px; width: 77px;
    left: 50%; transform: translateX(-50%);
  }
  .rule--light { top: 916px; background: var(--white); }
  .rule--dark { top: 494px; background: var(--grey-dark); }
  .site-url {
    position: absolute; left: 0; width: 100%; text-align: center;
    color: var(--white); font-weight: 300; font-size: 37px; letter-spacing: .5px;
  }
  .banner--brand .site-url { top: 968px; }
  .banner--services .site-url { top: 970px; }

  /* Services banner */
  .headline {
    position: absolute; top: 312px; left: 0; width: 100%;
    text-align: center; color: var(--grey-dark);
    font-weight: 700; font-size: 37px; line-height: 39px; letter-spacing: .5px;
  }
  .headline em { font-style: normal; color: var(--red); font-weight: 800; }
  .service-list {
    position: absolute; top: 542px; left: 44px; list-style: none;
  }
  .service-list li {
    display: flex; align-items: center; gap: 18px;
    height: 49px; color: var(--grey-mid);
    font-weight: 600; font-size: 28px; letter-spacing: .3px;
  }
  .service-list svg { width: 42px; height: 42px; flex: none; }
</style>
</head>
<body>
<main class="stage">

  <!-- Banner one: brand and slogan -->
  <section class="banner banner--brand">
    <svg class="banner-shapes" viewBox="0 0 367 1103" preserveAspectRatio="none">
      <defs>
        <linearGradient id="estateTones" x1="0" y1="0" x2="0" y2="1">
          <stop offset="0" stop-color="#5d7fa8"/>
          <stop offset=".45" stop-color="#8a7a66"/>
          <stop offset="1" stop-color="#2e3a2c"/>
        </linearGradient>
      </defs>
      <path d="M190 392 Q300 380 358 368 L358 388 Q280 398 190 392 Z" fill="var(--grey-dark)"/>
      <path d="M0 390 Q190 412 367 382 L367 592 Q170 590 0 622 Z" fill="url(#estateTones)" role="img" aria-label="Photo of a modern residential complex at dusk with lit garden paths"/>
      <path d="M10 612 Q150 586 367 582 L367 1103 L0 1103 L0 614 Z" fill="var(--red)"/>
    </svg>
    <div class="brand-mark">
      <div class="brand-mark__dot"></div>
      <p class="brand-mark__name">BRIGHTWELL<br>CONTRACTORS</p>
    </div>
    <p class="slogan">Safe<br>guarding<br>Communities<br>Electrical, Fire<br>&amp; Security<br>Solutions</p>
    <div class="rule rule--light"></div>
    <p class="site-url">bwc-kmo.com</p>
  </section>

  <!-- Banner two: services -->
  <section class="banner banner--services">
    <svg class="banner-shapes" viewBox="0 0 367 1103" preserveAspectRatio="none">
      <defs>
        <linearGradient id="warehouseTones" x1="0" y1="0" x2="1" y2="1">
          <stop offset="0" stop-color="#c9a35a"/>
          <stop offset=".55" stop-color="#8c6d4e"/>
          <stop offset="1" stop-color="#4c5c7c"/>
        </linearGradient>
        <linearGradient id="technicianTones" x1="0" y1="0" x2="1" y2="1">
          <stop offset="0" stop-color="#b3161c"/>
          <stop offset="1" stop-color="#6e0e12"/>
        </linearGradient>
      </defs>
      <path d="M0 0 H367 V232 Q180 252 0 222 Z" fill="url(#warehouseTones)" role="img" aria-label="Photo of a busy warehouse with a ceiling-mounted security camera"/>
      <path d="M0 222 Q180 252 367 232 L367 244 Q190 300 0 268 Z" fill="var(--red)"/>
      <path d="M20 832 Q180 798 367 810 L367 836 Q200 818 20 832 Z" fill="var(--grey-dark)"/>
      <path d="M0 846 Q190 820 367 836 L367 1103 L0 1103 Z" fill="url(#technicianTones)" role="img" aria-label="Red-tinted photo of an electrician working on a control panel"/>
    </svg>

    <h2 class="headline">WE HELP<br>OUR CLIENTS<br>GET <em>PEACE</em><br><em>OF MIND</em></h2>
    <div class="rule rule--dark"></div>

    <ul class="service-list">
      <li>
        <svg viewBox="0 0 42 42" aria-hidden="true"><circle cx="21" cy="21" r="18" fill="none" stroke="var(--red)" stroke-width="3.5"/><path d="M24 8 L13 23 H20 L17 34 L29 18 H22 Z" fill="var(--red)"/></svg>
        Electrical
      </li>
      <li>
        <svg viewBox="0 0 42 42" aria-hidden="true"><path d="M21 4 L36 10 V21 Q36 33 21 39 Q6 33 6 21 V10 Z" fill="none" stroke="var(--red)" stroke-width="3.5"/><path d="M13 21 L19 27 L30 15" fill="none" stroke="var(--red)" stroke-width="4" stroke-linecap="round" stroke-linejoin="round"/></svg>
        Security
      </li>
      <li>
        <svg viewBox="0 0 42 42" aria-hidden="true"><path d="M21 4 L36 10 V21 Q36 33 21 39 Q6 33 6 21 V10 Z" fill="none" stroke="var(--red)" stroke-width="3.5"/><path d="M14 27 H28 L26 24 V19 Q26 13 21 13 Q16 13 16 19 V24 Z" fill="var(--red)"/><circle cx="21" cy="30" r="2.2" fill="var(--red)"/></svg>
        Fire Protection
      </li>
      <li>
        <svg viewBox="0 0 42 42" aria-hidden="true"><g fill="var(--red)"><rect x="18" y="2" width="6" height="8"/><rect x="18" y="32" width="6" height="8"/><rect x="2" y="18" width="8" height="6"/><rect x="32" y="18" width="8" height="6"/><rect x="18" y="2" width="6" height="8" transform="rotate(45 21 21)"/><rect x="18" y="32" width="6" height="8" transform="rotate(45 21 21)"/><rect x="2" y="18" width="8" height="6" transform="rotate(45 21 21)"/><rect x="32" y="18" width="8" height="6" transform="rotate(45 21 21)"/></g><circle cx="21" cy="21" r="13" fill="var(--red)"/><circle cx="21" cy="18" r="4" fill="var(--white)"/><path d="M13 29 Q21 19 29 29 Z" fill="var(--white)"/></svg>
        Access Control
      </li>
      <li>
        <svg viewBox="0 0 42 42" aria-hidden="true"><rect x="4" y="6" width="26" height="24" rx="2" fill="none" stroke="var(--red)" stroke-width="3"/><path d="M14 12 L23 18 L14 24 Z" fill="var(--red)"/><path d="M33 18 V34" stroke="var(--red)" stroke-width="3"/><circle cx="30" cy="35" r="4" fill="var(--red)"/><path d="M33 18 L39 21" stroke="var(--red)" stroke-width="3"/></svg>
        Audio Video
      </li>
    </ul>

    <p class="site-url">bwc-kmo.com</p>
  </section>

</main>
</body>
</html>
```